Upscale Natural Ingredient based Skin Care Line for Children

Need a whimsical fun label and logo design for shower gel and body lotion for girls age 6 to 14 years old. The product will be sold in 6 oz Boston round clear bottles and labels should be 2.5"h x 6.9"w. I have attached some products that I think capture what I am looking for but am open to designs and creative labels. The product line is lulu Petal for Girls and colors should be very reflective of girls for that age group. Description of the shower Gel is:
Shower Gel
Description
Rise & Shine! Cheery natural cleansers restore skin’s radiance with a refreshing blend of Apricot Fruit & White Ginger. Extra hydrating Avocado Oils pour on the moisture, replenishing as they clarify, for skin that’s sunny & smooth with the perfect kiss of fragrance. To enjoy: Lather up & rinse away for spotless skin.

The Good Stuff
Paraben free, Phthalate free, Never animal tested, No artificial colors.

Description for the Lotion is:

Description
Super Smoother. Say goodbye to dry skin with this naturally nourishing dream cream. Soak up the sweet hydration! To enjoy: Formulated to absorb quickly. Dab on a dollop and dryness disappears.

Key Ingredients
A moisturizing medley of Cocoa Butter, Macadamia Nut & Olive Fruits meet pore pleasing Avocado Oil & Papaya Fruit to treat your body to moisture-rich bliss.

The Good Stuff
Paraben free, no phthalates, petrolatum, mineral oil, propylene glycol, retinol, sulfates, or synthetic color. Never animal tested.

Final design should be colorful with prints or images that she can relate too.

Target Market(s)

Girls age 6 to 14 years old. Product is nNatural based ingredients but very effective and smell great.

Logo Text

lulu Petal for Girls

Font styles to use
Decorative

Colors
f04a50
eea4c8
ffcf3e
faa54b
fbee3f
cadf82
86cfc6

Requirements
Must have
• Graphics / colors /collage of things that resonate with the demographic

```html
<!DOCTYPE html>
<html lang="en">
<head>
<meta charset="utf-8">
<title>lulu Petal – Lotion &amp; Shower Gel Labels</title>
<link rel="stylesheet" href="https://fonts.googleapis.com/css2?family=Josefin+Sans:wght@300;400;700&display=swap">
<style>
  :root {
    --canvas: #ffffff;
    --cream: #fbf8e4;
    --pattern-olive: #d3c43a;
    --pattern-pink: #f07cb8;
    --pattern-red: #c8283a;
    --label-pink: #fb56a8;
    --gold-light: #f6e08a;
    --gold: #d2a93f;
    --gold-dark: #8a6a1e;
    --brand-gold: #f4d566;
    --cream-text: #f9ee9c;
  }
  * { margin: 0; padding: 0; box-sizing: border-box; }
  html, body {
    width: 1200px;
    height: 448px;
    overflow: hidden;
    background: var(--canvas);
  }
  .sheet {
    width: 1200px;
    height: 448px;
    display: grid;
    grid-template-columns: 590px 590px;
    grid-template-rows: 214px 214px;
    column-gap: 8px;
    row-gap: 8px;
    padding: 6px;
    font-family: "Josefin Sans", sans-serif;
  }
  .label {
    position: relative;
    overflow: hidden;
  }
  .label__pattern {
    position: absolute;
    inset: 0;
    background:
      radial-gradient(ellipse 120px 90px at 6% 30%, rgba(240,124,184,.55), transparent 70%),
      radial-gradient(ellipse 140px 100px at 4% 85%, rgba(200,40,58,.35), transparent 70%),
      radial-gradient(ellipse 160px 110px at 30% 2%, rgba(211,196,58,.65), transparent 70%),
      radial-gradient(ellipse 150px 110px at 62% 0%, rgba(240,124,184,.5), transparent 70%),
      radial-gradient(ellipse 160px 110px at 90% 8%, rgba(211,196,58,.6), transparent 70%),
      radial-gradient(ellipse 130px 100px at 97% 50%, rgba(240,124,184,.5), transparent 70%),
      radial-gradient(ellipse 150px 100px at 92% 95%, rgba(200,40,58,.35), transparent 70%),
      radial-gradient(ellipse 170px 100px at 45% 100%, rgba(211,196,58,.65), transparent 70%),
      radial-gradient(ellipse 120px 90px at 72% 100%, rgba(240,124,184,.45), transparent 70%),
      radial-gradient(ellipse 140px 90px at 18% 100%, rgba(211,196,58,.55), transparent 70%),
      var(--cream);
  }
  .panel {
    position: absolute;
    background: var(--label-pink);
    border: 10px solid var(--gold);
    border-image: linear-gradient(120deg,
      var(--gold-light), var(--gold) 12%, var(--gold-dark) 22%, var(--gold-light) 34%,
      var(--gold) 46%, var(--gold-dark) 58%, var(--gold-light) 70%, var(--gold) 84%, var(--gold-dark)) 1;
    display: flex;
    flex-direction: column;
    align-items: center;
    justify-content: center;
    text-align: center;
  }
  .panel--front {
    left: 120px;
    top: 48px;
    width: 352px;
    height: 122px;
  }
  .panel--back {
    left: 48px;
    top: 40px;
    width: 490px;
    height: 134px;
    padding: 0 12px;
  }
  .brand-name {
    font-weight: 700;
    font-size: 46px;
    letter-spacing: 3px;
    line-height: 1;
    color: var(--brand-gold);
    text-transform: uppercase;
  }
  .product-name {
    margin-top: 12px;
    font-weight: 300;
    font-size: 19px;
    letter-spacing: 6px;
    color: var(--cream-text);
    text-transform: uppercase;
  }
  .description {
    font-weight: 300;
    font-size: 9px;
    line-height: 12.4px;
    letter-spacing: 1.2px;
    color: var(--cream-text);
  }
  .good-stuff {
    margin-top: 7px;
    font-weight: 400;
    font-size: 5.6px;
    letter-spacing: 1px;
    color: var(--cream-text);
    text-transform: uppercase;
  }
  .good-stuff__list {
    margin-top: 5px;
    font-weight: 400;
    font-size: 6.2px;
    letter-spacing: 1.1px;
    color: var(--cream-text);
    text-transform: uppercase;
  }
</style>
</head>
<body>
<main class="sheet">

  <section class="label label--lotion-front">
    <div class="label__pattern" role="img" aria-label="Retro floral print of olive, pink and red flowers and leaves on cream"></div>
    <div class="panel panel--front">
      <h1 class="brand-name">lulu Petal</h1>
      <p class="product-name">Lotion</p>
    </div>
  </section>

  <section class="label label--gel-front">
    <div class="label__pattern" role="img" aria-label="Retro floral print of olive, pink and red flowers and leaves on cream"></div>
    <div class="panel panel--front">
      <h1 class="brand-name">lulu Petal</h1>
      <p class="product-name">Shower Gel</p>
    </div>
  </section>

  <section class="label label--lotion-back">
    <div class="label__pattern" role="img" aria-label="Retro floral print of olive, pink and red flowers and leaves on cream"></div>
    <div class="panel panel--back">
      <p class="description">
        Super Smoother. Say goodbye to dry skin with this naturally<br>
        nourishing dream cream. Soak up the sweet hydration! To enjoy,<br>
        Dab on a dollop and dryness disappears.<br>
        Key Ingredients: a moisturizing medley of Cocoa Butter,<br>
        Macadamia Nut &amp; Olive Fruits meet pore pleasing Avocado<br>
        Oil &amp; Papaya Fruit to treat your body to moisture-rich bliss.
      </p>
      <p class="good-stuff">The Good Stuff</p>
      <p class="good-stuff__list">Paraben free, phthalate free, never animal tested, no artificial colors.</p>
    </div>
  </section>

  <section class="label label--gel-back">
    <div class="label__pattern" role="img" aria-label="Retro floral print of olive, pink and red flowers and leaves on cream"></div>
    <div class="panel panel--back">
      <p class="description">
        Rise &amp; Shine! Cheery natural cleansers restore skin's<br>
        radiance with a refreshing blend of Apricot Fruit &amp; White<br>
        Ginger. Extra hydrating Avocado Oils pour on the moisture,<br>
        replenishing as they clarify, for skin that's sunny &amp; smooth<br>
        with the perfect kiss of fragrance. To enjoy, lather up &amp;<br>
        rinse away for spotless skin.
      </p>
      <p class="good-stuff">The Good Stuff</p>
      <p class="good-stuff__list">Paraben free, phthalate free, never animal tested, no artificial colors.</p>
    </div>
  </section>

</main>
</body>
</html>
```